We need a business card for a company which is just starting up. The company name is Meridale Executive Services and we do a variety of things such as: support services for executives/leaders, sales team creation/management/training, and implementation of new programs to enhance a company's culture. The final design should be simple, professional and create a buzz of wanting to learn more. The owner is a woman of power, poise and leadership while she maintains qualities of caring, compassionate and honest. Her clients respect and refer her constantly. The colors are up for negotiation but should capture strength and softness at the same time. Possible colors: chocolate brown, dark pink, periwinkle. See attachment.

Target Market(s)

Medium to Large Businesses

Industry/Entity Type

Leadership

Requirements
Nice to have
• Qr code

```html
<!DOCTYPE html>
<html lang="en">
<head>
<meta charset="utf-8">
<title>Meridale Executive Services – Business Card</title>
<link rel="stylesheet" href="https://fonts.googleapis.com/css2?family=Italianno&family=Tinos:ital@1&display=swap">
<style>
  :root {
    --page: #ffffff;
    --card: #a46e78;
    --ink: #3b2227;
    --label: #111111;
    --motif-light: #7d5d62;
    --motif-dark: #3d272b;
    --glow: #d97a86;
  }
  * { margin: 0; padding: 0; box-sizing: border-box; }
  html, body {
    width: 1200px;
    height: 1200px;
    overflow: hidden;
    background: var(--page);
  }
  .sheet {
    position: relative;
    width: 1200px;
    height: 1200px;
  }
  .side-label {
    position: absolute;
    font-family: "Tinos", "Times New Roman", serif;
    font-style: italic;
    font-size: 60px;
    color: var(--label);
    line-height: 1;
  }
  .side-label--front { left: 875px; top: 86px; }
  .side-label--back { left: 138px; top: 990px; }

  .card {
    position: absolute;
    width: 801px;
    height: 447px;
    background: var(--card);
    color: var(--ink);
    font-family: "Italianno", cursive;
    overflow: hidden;
  }
  .card--front { left: 58px; top: 72px; }
  .card--back { left: 344px; top: 657px; }

  .motif {
    position: absolute;
  }
  .motif--band {
    left: 10px;
    top: 290px;
    width: 781px;
    height: 100px;
    background: linear-gradient(180deg, var(--motif-light) 0%, var(--motif-dark) 100%);
    box-shadow: 0 0 12px var(--glow);
  }
  .motif--feature {
    left: 84px;
    top: 120px;
    width: 217px;
    height: 210px;
    background: radial-gradient(ellipse at 50% 65%, var(--motif-dark) 0%, var(--motif-light) 100%);
    box-shadow: 0 0 16px var(--glow);
  }

  .company {
    position: absolute;
    left: 0;
    right: 0;
    top: 53px;
    text-align: center;
    font-size: 88px;
    line-height: 86px;
    font-weight: 400;
  }
  .tagline {
    position: absolute;
    left: 0;
    right: 0;
    top: 227px;
    text-align: center;
    font-size: 42px;
    line-height: 42px;
  }

  .contact {
    position: absolute;
    left: 292px;
    width: 440px;
    top: 88px;
    text-align: center;
  }
  .contact__name {
    font-size: 100px;
    line-height: 90px;
    font-weight: 400;
    white-space: nowrap;
  }
  .contact__role {
    font-size: 44px;
    line-height: 40px;
    margin-top: -12px;
  }
  .contact__lines {
    list-style: none;
    margin-top: 28px;
    font-size: 48px;
    line-height: 48px;
    white-space: nowrap;
  }
</style>
</head>
<body>
<main class="sheet">
  <span class="side-label side-label--front">FRONT</span>

  <section class="card card--front" aria-label="Card front">
    <div class="motif motif--band" role="img" aria-label="Row of decorative glowing circle motifs"></div>
    <h1 class="company">Meridale Executive<br>Services</h1>
    <p class="tagline">support-sales-implementation</p>
  </section>

  <section class="card card--back" aria-label="Card back">
    <div class="motif motif--feature" role="img" aria-label="Large decorative glowing circle motif"></div>
    <div class="contact">
      <h2 class="contact__name">Renata Lowell</h2>
      <p class="contact__role">owner</p>
      <ul class="contact__lines">
        <li>Phone (555) 555-5555</li>
        <li>www.website.com</li>
        <li>Email renata@email.com</li>
      </ul>
    </div>
  </section>

  <span class="side-label side-label--back">BACK</span>
</main>
</body>
</html>
```